Boutique Health and Fitness Personal Training Studio

I would like to have a brochure designed which provides a detailed description of the services offered in my business.
I have personal training studio, We look after people from early 20's to 90's, healthy to very unhealthy.
We conduct:
A consultation
An assessment
A personalised program
Personalised training sessions
I would like to base the design around the colours of my logo (attached) and use some of (or all of) the images and information I have also attached.
I would be happy with your own images included also.

Target Market(s)

20 to 90 year olds

Industry/Entity Type

Business

Font styles to use
Serif
Sans Serif

Colors
9bcb3c
add136
cadf82
eaf2ce

Requirements
Must have
• Colour and images of fitness.
• 8.5x14 legal
• Tri fold
• 2 folds with 3 faces back n front
Nice to have
• The feeling of wellbeing
Should not have
• This is not a gym.
• It should have the feel of a private relaxed environment

```html
<!DOCTYPE html>
<html lang="en">
<head>
<meta charset="utf-8">
<title>Evergreen Wellness Studio – Tri-fold Brochure</title>
<link href="https://fonts.googleapis.com/css2?family=Oswald:wght@500;600&family=Raleway:wght@400;500;600&display=swap" rel="stylesheet">
<style>
  :root {
    --green-deep: #4f8a1c;
    --green: #5e9e21;
    --green-bright: #6fb82a;
    --green-soft: #9bcb3c;
    --lime: #add136;
    --sage: #cadf82;
    --mist: #eaf2ce;
    --ink: #2b2b2b;
    --paper: #ffffff;
    --backdrop: #e4e4e4;
  }
  * { box-sizing: border-box; margin: 0; padding: 0; }
  html, body { width: 1000px; height: 1200px; overflow: hidden; }
  body {
    background: var(--backdrop);
    font-family: "Raleway", Arial, sans-serif;
    color: var(--ink);
    position: relative;
  }
  .sheet {
    position: absolute;
    left: 20px;
    width: 960px;
    height: 580px;
    background: var(--paper);
    overflow: hidden;
    box-shadow: 0 6px 18px rgba(0,0,0,.18);
  }
  .sheet--outside { top: 12px; }
  .sheet--inside { top: 608px; }
  .sheet svg.shapes { position: absolute; inset: 0; }
  .fold {
    position: absolute; top: 0; bottom: 0; width: 1px;
    background: rgba(0,0,0,.06);
  }
  .block { position: absolute; }
  .heading {
    font-family: "Oswald", "Arial Narrow", sans-serif;
    font-weight: 600;
    text-transform: uppercase;
    line-height: 1.05;
    color: var(--green);
  }
  .heading--light { color: var(--paper); }
  .copy { font-size: 12.5px; line-height: 1.45; }
  .copy--light { color: var(--paper); font-size: 11.5px; }
  .copy--right { text-align: right; }
  .copy--center { text-align: center; }

  /* outside */
  .program { left: 26px; top: 22px; width: 270px; }
  .program .heading { font-size: 21px; margin-bottom: 6px; }
  .nutrition { left: 22px; top: 338px; width: 280px; }
  .nutrition .heading { font-size: 21px; margin-bottom: 8px; }
  .sessions { left: 392px; top: 96px; width: 200px; text-align: center; }
  .sessions .heading { font-size: 20px; margin-bottom: 6px; }
  .fund { left: 440px; top: 310px; width: 180px; text-align: right; }
  .fund .heading { font-size: 19px; }
  .fund .open { font-family: "Oswald", sans-serif; font-weight: 500; font-size: 18px; text-transform: uppercase; color: var(--ink); }
  .price { left: 344px; top: 378px; display: flex; align-items: center; gap: 6px; }
  .price .small { font-size: 10.5px; line-height: 1.2; text-transform: uppercase; font-weight: 600; }
  .price .amount { font-family: "Oswald", sans-serif; font-weight: 600; font-size: 40px; color: var(--green); line-height: 1; }
  .parking { left: 340px; top: 434px; width: 280px; text-align: center; }
  .parking .heading { font-size: 19px; margin-bottom: 8px; }
  .address { font-size: 12px; line-height: 1.45; }
  .brand { left: 676px; top: 334px; display: flex; align-items: center; gap: 10px; }
  .brand .mark { width: 30px; height: 30px; border-radius: 50%; background: var(--green); flex: none; }
  .brand .name { font-family: "Raleway", sans-serif; font-weight: 600; font-size: 19px; color: var(--green); line-height: 1.15; width: 170px; }
  .tagline { left: 660px; top: 404px; width: 270px; text-align: center; }
  .tagline .heading { font-size: 21px; margin-bottom: 10px; }

  /* inside */
  .caring { left: 18px; top: 86px; width: 250px; }
  .caring .heading { font-size: 18px; margin-bottom: 6px; }
  .expect { left: 100px; top: 242px; width: 210px; }
  .expect .heading { font-size: 21px; margin-bottom: 8px; text-align: right; }
  .expect .copy { font-size: 12px; line-height: 1.4; }
  .expect .copy + .copy { margin-top: 10px; }
  .consult { left: 336px; top: 242px; width: 290px; }
  .consult .heading { font-size: 21px; margin-bottom: 8px; }
  .assess { left: 700px; top: 112px; width: 240px; }
  .assess .heading { font-size: 21px; margin-bottom: 8px; text-align: right; }
</style>
</head>
<body>

<!-- Outside of the tri-fold -->
<section class="sheet sheet--outside">
  <svg class="shapes" width="960" height="580" viewBox="0 0 960 580">
    <defs>
      <linearGradient id="skin" x1="0" y1="0" x2="1" y2="1">
        <stop offset="0" stop-color="#e9e3da"/><stop offset="1" stop-color="#c9b59f"/>
      </linearGradient>
      <linearGradient id="portrait" x1="0" y1="0" x2="1" y2="1">
        <stop offset="0" stop-color="#eef0e6"/><stop offset=".6" stop-color="#c8c2b4"/><stop offset="1" stop-color="#9a9a8c"/>
      </linearGradient>
      <linearGradient id="silhouette" x1="0" y1="0" x2="0" y2="1">
        <stop offset="0" stop-color="#3d6b15"/><stop offset="1" stop-color="#1d2a10"/>
      </linearGradient>
      <linearGradient id="gymdark" x1="0" y1="0" x2="1" y2="1">
        <stop offset="0" stop-color="#6b5a4d"/><stop offset="1" stop-color="#1e1a18"/>
      </linearGradient>
    </defs>
    <!-- left panel -->
    <polygon points="0,0 320,0 320,110 130,318 0,190" fill="var(--green)"/>
    <polygon points="50,150 250,150 230,240 135,300 60,230" fill="url(#silhouette)" role="img" aria-label="Silhouettes of a trainer and a client standing side by side"/>
    <polygon points="250,230 320,275 290,330 220,300" fill="#c23a2a" role="img" aria-label="Photo of a tape measure around a waist"/>
    <polygon points="230,580 320,495 320,580" fill="url(#gymdark)" role="img" aria-label="Photo of an arm lifting a dumbbell"/>
    <!-- middle panel -->
    <polygon points="320,0 470,0 400,70 320,70" fill="url(#skin)" role="img" aria-label="Photo of a woman exercising with light weights"/>
    <polygon points="480,0 560,0 520,60" fill="#d9dfe3" role="img" aria-label="Photo of a group exercise class"/>
    <polygon points="340,185 490,35 640,35 640,220 565,298 470,298" fill="var(--green-bright)"/>
    <polygon points="602,262 640,225 640,298" fill="#d7dde6" role="img" aria-label="Photo of a hand holding a blue dumbbell"/>
    <polygon points="595,580 640,535 640,580" fill="var(--green)"/>
    <!-- right panel -->
    <polygon points="640,0 960,0 960,250 890,318 810,250 640,250" fill="url(#portrait)" role="img" aria-label="Portrait photo of a man in a training singlet"/>
    <polygon points="910,300 960,255 960,390" fill="var(--green)"/>
  </svg>
  <div class="fold" style="left:320px"></div>
  <div class="fold" style="left:640px"></div>

  <div class="block program">
    <h2 class="heading heading--light">The Program</h2>
    <p class="copy copy--light">Your program will be designed with consideration to your health and fitness background, your objectives and your strengths and weaknesses. It will be personally tailored to your needs and provide you with a plan to focus your energies on.</p>
  </div>

  <div class="block nutrition">
    <h2 class="heading">Nutrition</h2>
    <p class="copy">Nutrition is central to an effective program, as it will provide you with maximal energy for exercise as well as keeping yourself lean and healthy for a long term fitter lifestyle. Evergreen Wellness Studio provides initial monitoring and ongoing modification in accordance with your needs.</p>
  </div>

  <div class="block sessions">
    <h2 class="heading heading--light">Your Sessions</h2>
    <p class="copy copy--light">Training at the studio is professional and caring, but focused and challenging. Typically each session will take approximately 60 minutes. Training times can be organized to suit your needs with early mornings and evenings available.</p>
  </div>

  <div class="block fund">
    <p class="heading">Health Fund<br>Claimable</p>
    <p class="open">Open 7 Days</p>
  </div>

  <div class="block price">
    <span class="small">The cost</span>
    <span class="amount">$45</span>
    <span class="small">Paid in<br>blocks of<br>5 or 10<br>sessions.</span>
  </div>

  <div class="block parking">
    <h2 class="heading">Ample Private Parking Available</h2>
    <p class="address">Evergreen Wellness Studio<br>Unit 12, Level 2<br>8 Wattle Grove Road, Fernhill<br>Ph: 0400 000 123<br>www.evergreenwellness.com.au</p>
  </div>

  <div class="block brand">
    <span class="mark"></span>
    <span class="name">Evergreen Wellness Studio</span>
  </div>

  <div class="block tagline">
    <h1 class="heading">Personalised Care in Fitness and Health</h1>
    <p class="copy">Exercise programs for all levels of health and fitness and all age groups. Experience in managing a wide range of chronic health conditions.</p>
  </div>
</section>

<!-- Inside of the tri-fold -->
<section class="sheet sheet--inside">
  <svg class="shapes" width="960" height="580" viewBox="0 0 960 580">
    <defs>
      <linearGradient id="warm" x1="0" y1="0" x2="1" y2="1">
        <stop offset="0" stop-color="#efe6dc"/><stop offset="1" stop-color="#c9a98c"/>
      </linearGradient>
      <linearGradient id="food" x1="0" y1="0" x2="1" y2="1">
        <stop offset="0" stop-color="#7aa83a"/><stop offset=".5" stop-color="#e0b32e"/><stop offset="1" stop-color="#7b6a5c"/>
      </linearGradient>
      <linearGradient id="shadowfig" x1="0" y1="0" x2="0" y2="1">
        <stop offset="0" stop-color="#2a2a2a"/><stop offset="1" stop-color="#0e0e0e"/>
      </linearGradient>
    </defs>
    <!-- left panel -->
    <polygon points="0,80 300,0 320,0 320,150 190,262 0,282" fill="var(--green-bright)"/>
    <polygon points="40,232 72,200 104,232 72,264" fill="var(--paper)"/>
    <polygon points="0,410 90,400 92,580 0,580" fill="url(#shadowfig)" opacity=".92" role="img" aria-label="Silhouette of a trainer guiding a client through a lunge"/>
    <!-- middle panel -->
    <polygon points="290,20 330,0 400,0 320,60" fill="var(--green)"/>
    <polygon points="320,60 380,40 440,120 360,170" fill="url(#warm)" role="img" aria-label="Photo of a smiling mature woman exercising"/>
    <polygon points="420,40 500,0 560,90 470,160" fill="#c8322c" role="img" aria-label="Photo of a practitioner assessing a client's back"/>
    <polygon points="520,0 640,60 600,100 540,60" fill="var(--green-soft)"/>
    <polygon points="400,170 450,150 480,200 430,222" fill="var(--green)"/>
    <polygon points="580,170 640,130 640,215" fill="#b78f6a" role="img" aria-label="Photo of two women chatting after training"/>
    <polygon points="340,420 380,400 410,440 370,460" fill="var(--green-bright)"/>
    <polygon points="392,462 430,442 458,480 420,500" fill="var(--green)"/>
    <polygon points="340,510 400,490 440,565 380,580" fill="#e3e8ee" role="img" aria-label="Photo of a woman training on a cable machine"/>
    <!-- right panel -->
    <polygon points="660,40 710,0 790,0 730,85" fill="url(#food)" role="img" aria-label="Photo of fresh vegetables, dumbbells and a water bottle"/>
    <polygon points="682,100 960,60 960,300 830,430 692,300" fill="var(--green)"/>
    <polygon points="800,320 850,272 900,320 850,368" fill="var(--paper)"/>
    <polygon points="470,420 960,385 960,580 470,580" fill="url(#shadowfig)" opacity=".92" role="img" aria-label="Silhouette of a woman balancing on a trainer's back over an exercise ball"/>
  </svg>
  <div class="fold" style="left:320px"></div>
  <div class="fold" style="left:640px"></div>

  <div class="block caring">
    <h2 class="heading heading--light">Experienced Professionals Caring for Your Wellbeing</h2>
    <p class="copy copy--light">Exercise Physiologist with over 25 years of experience managing the health and fitness needs of the community.</p>
  </div>

  <div class="block expect">
    <h2 class="heading">What<br>to Expect</h2>
    <p class="copy copy--right">On arrival at the studio you will be asked to complete a questionnaire, which will provide us with information regarding your background with health and fitness, as well as your goals and objectives.</p>
    <p class="copy copy--right">Please bring any relevant medical information from medical practitioners or health professionals that you feel may impact on your program.</p>
  </div>

  <div class="block consult">
    <h2 class="heading">Consultation</h2>
    <p class="copy">A consultation will allow you to share your thoughts, concerns and objectives, as well as provide you with ample opportunity to expand on the answers from your questionnaire relating to your prior and current health, medical and physical concerns.</p>
  </div>

  <div class="block assess">
    <h2 class="heading heading--light">Assessment</h2>
    <p class="copy copy--light copy--center">An assessment will be conducted to provide us both with a baseline measure of your cardiovascular fitness, strength, flexibility, balance and body composition measures. These measures provide us with a reference for program design and also to indicate improvements along the way.</p>
  </div>
</section>

</body>
</html>
```